Flyer Design Project

I require a double sided flyer in PSD format.
The flyer should look fresh and clean.
The flyer is for an digital marketing company that offers various services. The services are broken down into 3 main categories and the design should reflect this.
All the content is provided in the attached file
Industry/Entity Type
Digital
Requirements
Must have
- Front of the leaflet to be mainly white background with appealing text based questions in the colours in large font with relevant images.
Back if the
3 separate boxes using the colours indicated in the attachment for the services on back of the leafet.
Should not have
- Gradients
Borders on the edges of the design
Vignettes
Black elements
Any text below 10pt
Fancy fonts
Do not use old-style fonts

```html
<!DOCTYPE html>
<html lang="en">
<head>
<meta charset="utf-8">
<title>Lumora Digital Marketing Flyer</title>
<link rel="stylesheet" href="https://fonts.googleapis.com/css2?family=Francois+One&family=Arimo:wght@400;700&display=swap">
<style>
  :root{
    --stage:#1c1c1c;
    --paper:#ffffff;
    --lime:#a6cc3a;
    --lime-band:#c6da3c;
    --sky:#2fbdec;
    --amber:#f7972f;
    --sun:#fcbf3f;
    --coupon-green:#1f9b46;
    --coupon-blue:#1a6bb8;
    --coupon-orange:#ee6e21;
    --dash:#1d3f7a;
    --grey:#9a9a9a;
    --grey-dark:#6f6f6f;
    --ink-blue:#1b6db5;
    --white:#ffffff;
    --head:"Francois One", "Arial Narrow", sans-serif;
    --body:"Arimo", Arial, sans-serif;
  }
  *{box-sizing:border-box;margin:0;padding:0}
  html,body{width:1200px;height:738px;overflow:hidden}
  body{background:var(--stage);position:relative;font-family:var(--body)}

  /* ---------- Front ---------- */
  .flyer-front{position:absolute;left:70px;top:84px;width:430px;height:570px;background:var(--paper);overflow:hidden}
  .hero-art{position:absolute;left:0;top:0;width:430px;height:232px;
    background:linear-gradient(160deg,#ffffff 0%,#e9edf0 40%,#7a7f86 75%,#2d2f33 100%)}
  .band{position:absolute;left:-10px;width:450px;transform:skewY(-2.5deg);color:var(--white);font-family:var(--head);text-transform:uppercase;line-height:1}
  .band-lime{top:228px;height:78px;background:var(--lime-band);padding:12px 0 0 90px}
  .band-sky{top:314px;height:40px;background:var(--sky);padding:5px 0 0 58px}
  .band-sun{top:362px;height:74px;background:var(--sun);padding:10px 90px 0 0;text-align:right}
  .band .small{font-size:10px;letter-spacing:.5px;display:block}
  .band .large{font-size:27px;display:block}
  .band .mid{font-size:18px;display:block}
  .band-lime .indent{padding-left:40px}
  .band-sky .large{font-size:21px}

  .help-line{position:absolute;left:72px;top:476px;font-family:var(--head);color:var(--grey-dark);font-size:16px;line-height:1.25;text-transform:uppercase;text-align:right;width:210px}
  .brand-disc{position:absolute;border-radius:50%;background:var(--grey);color:var(--white);font-family:var(--head);display:flex;align-items:center;justify-content:center}
  .flyer-front .brand-disc{left:300px;top:440px;width:92px;height:92px;font-size:20px}
  .call-bar{position:absolute;background:var(--grey);color:var(--white);font-weight:700;font-family:var(--body);text-align:center}
  .flyer-front .call-bar{left:30px;top:536px;width:396px;height:22px;font-size:14px;line-height:22px}

  /* ---------- Back ---------- */
  .flyer-back{position:absolute;left:540px;top:170px;width:600px;height:400px;background:var(--paper)}
  .service{position:absolute;top:20px;width:150px;height:300px;color:var(--white);padding:10px 10px 0}
  .service-consulting{left:26px;background:var(--lime)}
  .service-design{left:222px;background:var(--sky)}
  .service-sem{left:418px;background:var(--amber)}
  .service h2{font-family:var(--head);font-weight:400;text-align:center;font-size:26px;line-height:1;text-transform:uppercase}
  .service h2 span{display:block;font-size:18px;margin-top:3px}
  .service ul{list-style:none;margin-top:14px;font-weight:700;font-size:11px}
  .service li{display:flex;gap:5px;margin-bottom:13px;line-height:1.2}
  .service-sem ul{margin-top:8px;font-size:10.5px}
  .service-sem li{margin-bottom:2px;gap:4px;line-height:1.15}
  .tick{flex:0 0 10px;width:10px;height:10px;margin-top:1px}
  .coupon{position:absolute;left:10px;right:10px;bottom:12px;height:82px;border:2px dashed var(--dash);color:var(--white);text-align:center;font-family:var(--body);font-weight:700;padding-top:6px;white-space:nowrap}
  .coupon-green{background:var(--coupon-green)}
  .coupon-blue{background:var(--coupon-blue)}
  .coupon-orange{background:var(--coupon-orange);padding-top:8px}
  .coupon .big{display:block;font-size:38px;line-height:1}
  .coupon .sub{display:block;font-size:16px;margin-top:5px}
  .coupon-orange .big{font-family:var(--head);font-weight:400;font-size:32px}
  .coupon-orange .sub{font-family:var(--head);font-weight:400;font-size:16px;margin-top:4px}
  .scissors{position:absolute;right:-4px;top:-12px;width:14px;height:12px}

  .flyer-back .brand-disc{left:76px;top:332px;width:56px;height:56px;font-size:13px}
  .divider{position:absolute;left:160px;top:330px;width:1px;height:58px;background:var(--ink-blue)}
  .address{position:absolute;left:182px;top:332px;color:var(--ink-blue);font-size:12px;line-height:1.2;font-style:normal}
  .address strong{font-size:14px;display:block}
  .flyer-back .call-bar{left:306px;top:330px;width:270px;height:54px;padding-top:6px}
  .flyer-back .call-bar .num{display:block;font-size:22px;line-height:1.1}
  .flyer-back .call-bar .tag{display:block;font-size:14px}
</style>
</head>
<body>
<svg width="0" height="0" style="position:absolute" aria-hidden="true">
  <defs>
    <symbol id="tick" viewBox="0 0 10 10">
      <rect x=".5" y=".5" width="9" height="9" fill="none" stroke="#fff"/>
      <path d="M2 5 L4.2 7.2 L8.5 2.5" fill="none" stroke="#fff" stroke-width="1.4"/>
    </symbol>
    <symbol id="scissors" viewBox="0 0 14 12">
      <circle cx="3" cy="9" r="2" fill="none" stroke="#fff" stroke-width="1.2"/>
      <circle cx="8" cy="10" r="2" fill="none" stroke="#fff" stroke-width="1.2"/>
      <path d="M4 7.5 L12 1 M7 8 L9 1" stroke="#fff" stroke-width="1.2"/>
    </symbol>
  </defs>
</svg>

<section class="flyer-front">
  <div class="hero-art" role="img" aria-label="Illustration of a highway made of cursor arrows leading to a laptop, under a road sign reading Website Traffic"></div>

  <div class="band band-lime">
    <span class="small">Did you know</span>
    <span class="large">85% of consumers</span>
    <span class="small indent">use the internet</span>
    <span class="mid indent">to find businesses like yours?</span>
  </div>
  <div class="band band-sky">
    <span class="small">Are your</span>
    <span class="large">Customers finding you online?</span>
  </div>
  <div class="band band-sun">
    <span class="small">Do you need</span>
    <span class="large">More customers</span>
    <span class="small">for your business?</span>
  </div>

  <p class="help-line">Let us help you<br>grow your business online</p>
  <div class="brand-disc">Lumora</div>
  <div class="call-bar">Call 0121 496 0183 for a FREE consultation</div>
</section>

<section class="flyer-back">
  <article class="service service-consulting">
    <h2>Consulting<span>Services</span></h2>
    <ul>
      <li><svg class="tick"><use href="#tick"/></svg>Marketing Strategy And Planning</li>
      <li><svg class="tick"><use href="#tick"/></svg>Business Branding</li>
      <li><svg class="tick"><use href="#tick"/></svg>Competition Analysis</li>
    </ul>
    <div class="coupon coupon-green">
      <svg class="scissors"><use href="#scissors"/></svg>
      <span class="big">FREE</span><span class="sub">Consultation</span>
    </div>
  </article>

  <article class="service service-design">
    <h2>Design<span>Services</span></h2>
    <ul>
      <li><svg class="tick"><use href="#tick"/></svg>Web Design</li>
      <li><svg class="tick"><use href="#tick"/></svg>Website Maintenance</li>
      <li><svg class="tick"><use href="#tick"/></svg>Logo Design</li>
      <li><svg class="tick"><use href="#tick"/></svg>Flyer Design</li>
    </ul>
    <div class="coupon coupon-blue">
      <svg class="scissors"><use href="#scissors"/></svg>
      <span class="big">FREE</span><span class="sub">Website</span>
    </div>
  </article>

  <article class="service service-sem">
    <h2>SEM<span>Services</span></h2>
    <ul>
      <li><svg class="tick"><use href="#tick"/></svg>Local Business Marketing</li>
      <li><svg class="tick"><use href="#tick"/></svg>Ppc</li>
      <li><svg class="tick"><use href="#tick"/></svg>Email Marketing</li>
      <li><svg class="tick"><use href="#tick"/></svg>Seo</li>
      <li><svg class="tick"><use href="#tick"/></svg>Social Media</li>
      <li><svg class="tick"><use href="#tick"/></svg>Content Development</li>
      <li><svg class="tick"><use href="#tick"/></svg>Website Audit</li>
      <li><svg class="tick"><use href="#tick"/></svg>Lead Generation</li>
    </ul>
    <div class="coupon coupon-orange">
      <svg class="scissors"><use href="#scissors"/></svg>
      <span class="big">25% OFF</span><span class="sub">any SEM Package</span>
    </div>
  </article>

  <div class="brand-disc">Lumora</div>
  <div class="divider"></div>
  <address class="address"><strong>Lumora</strong>12 Canal Quay<br>Ashford Vale<br>AV4 7QR</address>
  <div class="call-bar"><span class="num">Call 0121 496 0000</span><span class="tag">for a FREE consultation</span></div>
</section>
</body>
</html>
```